Kestrel Gardenworks Business Card

An eye catching, yet simple business card that includes;

1. our logo
2. office phone - 5083172946
3. email - kestrelgardenworks@mailbrook.com
4. website - www.kestrelgardenworks.com
5. instagram - @kestrelgardenworksnv

```html
<!DOCTYPE html>
<html lang="en">
<head>
<meta charset="utf-8">
<title>Kestrel Gardenworks Business Card</title>
<link rel="stylesheet" href="https://fonts.googleapis.com/css2?family=Montserrat:wght@600;800&display=swap">
<style>
  :root {
    --backdrop: #808080;
    --card: #ffffff;
    --earth: #9e5d2b;
    --charcoal: #1f1a17;
    --on-earth: #ffffff;
  }
  html, body {
    margin: 0;
    padding: 0;
    width: 1200px;
    height: 1000px;
    overflow: hidden;
    background: var(--backdrop);
  }
  .business-card {
    position: absolute;
    left: 136px;
    top: 228px;
    width: 929px;
    height: 543px;
    background: var(--card);
    overflow: hidden;
    font-family: "Montserrat", sans-serif;
  }
  .card-waves {
    position: absolute;
    inset: 0;
    width: 929px;
    height: 543px;
  }
  .wave-earth { fill: var(--earth); }
  .wave-swoosh { fill: var(--charcoal); }
  .brand {
    position: absolute;
    left: 62px;
    top: 86px;
    display: flex;
    align-items: center;
    gap: 18px;
    color: var(--charcoal);
    font-weight: 800;
  }
  .brand-dot {
    width: 64px;
    height: 64px;
    border-radius: 50%;
    background: var(--earth);
    flex: none;
  }
  .brand-name {
    margin: 0;
    font-size: 46px;
    line-height: 1.05;
    font-weight: 800;
    letter-spacing: 0.5px;
  }
  .brand-name span { display: block; }
  .brand-name .brand-line-2 {
    font-size: 33px;
    letter-spacing: 3px;
  }
  .contact-list {
    position: absolute;
    left: 384px;
    top: 366px;
    margin: 0;
    padding: 0;
    list-style: none;
    color: var(--on-earth);
    font-size: 23px;
    font-weight: 600;
    line-height: 35.5px;
    white-space: nowrap;
  }
</style>
</head>
<body>
  <article class="business-card">
    <svg class="card-waves" viewBox="0 0 929 543" aria-hidden="true">
      <path class="wave-swoosh" d="M305,322 Q600,240 929,240 V337 C900,290 820,264 700,264 Q520,264 305,322 Z"/>
      <path class="wave-earth" d="M0,429 Q450,290 694,290 C880,290 929,360 929,430 V543 H0 Z"/>
    </svg>

    <header class="brand">
      <div class="brand-dot"></div>
      <h1 class="brand-name"><span>Kestrel</span><span class="brand-line-2">GARDENWORKS</span></h1>
    </header>

    <ul class="contact-list">
      <li>office phone - 5083172946</li>
      <li>email - kestrelgardenworks@mailbrook.com</li>
      <li>website - www.kestrelgardenworks.com</li>
      <li>instagram - @kestrelgardenworksnv</li>
    </ul>
  </article>
</body>
</html>
```